Business card for biotech sales agent

I need a logo and business card designed for my company Belunor. We work in partnership with Kestrel Group. Kestrel have developed advanced biotech. Their hand sanitiser is alcohol free and works for 24 hours on skin, even with regular hand washing. The surface sanitiser works for up to 30 days on surfaces and fabrics. Its food-safe, it's non-toxic, safe for animals and humans. The products have a very wide variety of applications: everything from agri-business, hotels, hospitality, schools, child and baby care, transport, meat processing etc.<br/>I would like my design to use blues or green-blues and communicate a bit of nano-tech but also trust and safety.<br/>I would also use the Kestrel logo on my card next to 'sales & distribution agent'

Target Market(s)

B2B, selling to FMCG and large companies such as airlines

Industry/Entity Type

Biotechnology

Contact Information for Business Card

Helen Pritch
Director

Phone: +64 22 519 3064
Email: helen@belunor.co
www.belunor.co
7 Tamsin St, Newmarket, Auckland, New Zealand 1023

Font styles to use
Sans Serif

Colors
3276b5
33b8a4
34a7d8
3176b5
ffffff

Requirements
Must have
• Not be too busy, clean space is good
• A logo styling to the word Belunor
Nice to have
• A little bit of a bio-tech image as a screen perhaps

```html
<!DOCTYPE html>
<html lang="en">
<head>
<meta charset="utf-8">
<title>Belunor Business Card</title>
<link rel="stylesheet" href="https://fonts.googleapis.com/css2?family=Poppins:wght@300;400;500&display=swap">
<style>
  :root {
    --page-bg: #4a5d72;
    --brand-blue: #05457f;
    --paper: #ffffff;
    --ink-soft: #c9d6e6;
  }
  * { box-sizing: border-box; margin: 0; padding: 0; }
  html, body {
    width: 1200px; height: 900px; overflow: hidden;
    background: var(--page-bg);
    font-family: "Poppins", sans-serif;
  }
  .sheet {
    width: 1200px; height: 900px;
    display: flex; flex-direction: column; align-items: center; justify-content: center;
    gap: 50px;
  }
  .card {
    position: relative;
    width: 630px; height: 360px;
    box-shadow: 0 10px 30px rgba(0,0,0,.25);
    overflow: hidden;
  }

  /* Front */
  .card-front { background: var(--paper); color: var(--brand-blue); }
  .brand-front {
    position: absolute; top: 48px; left: 0; width: 100%;
    display: flex; align-items: center; justify-content: center; gap: 16px;
  }
  .brand-square { width: 46px; height: 46px; background: var(--brand-blue); }
  .brand-name {
    font-weight: 400; font-size: 40px; letter-spacing: 6px; text-transform: uppercase;
    line-height: 1;
  }
  .name-band {
    position: absolute; top: 132px; left: 0; width: 100%; height: 72px;
    background: var(--brand-blue); color: var(--paper);
    display: flex; flex-direction: column; align-items: center; justify-content: center;
  }
  .person-name { font-size: 26px; font-weight: 400; letter-spacing: .5px; line-height: 1.1; }
  .person-title { font-size: 12px; font-weight: 300; letter-spacing: .5px; }
  .contact-list {
    position: absolute; left: 48px; bottom: 44px;
    list-style: none; font-size: 13px; line-height: 1.65;
  }
  .contact-list li { display: flex; align-items: center; gap: 8px; }
  .contact-list svg { width: 12px; height: 12px; flex: none; }
  .address {
    position: absolute; right: 48px; bottom: 60px;
    font-size: 13px; line-height: 1.5; font-style: normal;
  }

  /* Back */
  .card-back { background: var(--brand-blue); color: var(--paper); }
  .brand-back {
    position: absolute; top: 130px; left: 110px;
    display: flex; flex-direction: column; align-items: center; gap: 16px;
  }
  .brand-back .brand-square { background: var(--paper); width: 44px; height: 44px; }
  .brand-back .brand-name { font-size: 38px; font-weight: 300; letter-spacing: 8px; }
  .web-mark {
    position: absolute; left: 190px; bottom: 36px;
    font-size: 12px; font-weight: 300; letter-spacing: 4px; color: var(--ink-soft);
  }
</style>
</head>
<body>
<main class="sheet">
  <section class="card card-front" aria-label="Business card front">
    <div class="brand-front">
      <span class="brand-square"></span>
      <span class="brand-name">Belunor</span>
    </div>
    <div class="name-band">
      <p class="person-name">Helen Pritch</p>
      <p class="person-title">Director</p>
    </div>
    <ul class="contact-list">
      <li>
        <svg viewBox="0 0 12 12" aria-hidden="true"><path d="M3 1l2 2.5-1.2 1.2a7 7 0 0 0 3.5 3.5L8.5 7 11 9l-1.3 1.8C5.5 10.5 1.5 6.5 1.2 2.3z" fill="currentColor"/></svg>
        Phone: +64 22 519 3064
      </li>
      <li>
        <svg viewBox="0 0 12 12" aria-hidden="true"><rect x="1" y="2.5" width="10" height="7" fill="none" stroke="currentColor" stroke-width="1.2"/><path d="M1 3l5 3.5L11 3" fill="none" stroke="currentColor" stroke-width="1.2"/></svg>
        Email: helen@belunor.co
      </li>
      <li>
        <svg viewBox="0 0 12 12" aria-hidden="true"><circle cx="6" cy="6" r="5" fill="none" stroke="currentColor" stroke-width="1.1"/><ellipse cx="6" cy="6" rx="2.2" ry="5" fill="none" stroke="currentColor" stroke-width="1"/><path d="M1 6h10" stroke="currentColor" stroke-width="1"/></svg>
        www.belunor.co
      </li>
    </ul>
    <address class="address">
      7 Tamsin St,<br>
      Corwen Heights, Ashby,<br>
      New Zealand 4817
    </address>
  </section>

  <section class="card card-back" aria-label="Business card back">
    <div class="brand-back">
      <span class="brand-square"></span>
      <span class="brand-name">Belunor</span>
    </div>
    <p class="web-mark">www.belunor.co</p>
  </section>
</main>
</body>
</html>
```